Got the awesome logo, now need the awesome business card

Want to use my just purchased logo on the backside of my card and to secure another logo by the same designer (Marek) for the front side.

Reason: I have uploaded the logos. LOX4 should be on the front of the card with my contact information and Lox4ane should be on the back. Thank you.

The logos have been uploaded and I have extended the deadline by 5 days. The LOX$ logo should be on the front with my contact information and the lox4ane should be on the back.

Business

• Existing logo(s), clean background on front of card

```html
<!DOCTYPE html>
<html lang="en">
<head>
<meta charset="utf-8">
<title>Lox4 Management – Business Card</title>
<link href="https://fonts.googleapis.com/css2?family=Mulish:wght@400;700&display=swap" rel="stylesheet">
<style>
  :root {
    --page-bg: #d9d9d6;
    --brand-blue: #1f6fb6;
    --brand-blue-dark: #175a96;
    --brand-orange: #f28a1e;
    --ink-grey: #5a5a5a;
    --card-white: #ffffff;
    --panel-dark: #2f3133;
    --panel-dark-edge: #3c3e41;
    --text-light: #f2f2f2;
    --text-muted: #c9c9c9;
  }
  * { margin: 0; padding: 0; box-sizing: border-box; }
  html, body { width: 1200px; height: 871px; overflow: hidden; }
  body {
    background: var(--page-bg);
    font-family: "Mulish", Arial, sans-serif;
    position: relative;
  }
  .card {
    position: absolute;
    width: 560px;
    height: 320px;
    border-radius: 4px;
    overflow: hidden;
    box-shadow: 0 6px 18px rgba(0,0,0,0.18);
  }

  /* Back side */
  .card-back {
    left: 90px; top: 90px;
    background: linear-gradient(160deg, #2c86cc 0%, var(--brand-blue) 55%, var(--brand-blue-dark) 100%);
    display: flex; flex-direction: column; align-items: center; justify-content: center;
  }
  .back-wordmark {
    font-weight: 700;
    font-size: 84px;
    letter-spacing: -1px;
    color: var(--card-white);
    line-height: 1;
  }
  .back-tagline {
    margin-top: 8px;
    font-weight: 400;
    font-size: 26px;
    color: var(--ink-grey);
    letter-spacing: 0.5px;
  }

  /* Front side */
  .card-front {
    left: 550px; top: 460px;
    background: var(--card-white);
  }
  .front-divider { position: absolute; inset: 0; }
  .front-logo {
    position: absolute; left: 40px; top: 92px;
    display: flex; flex-direction: column;
  }
  .front-wordmark {
    font-weight: 700;
    font-size: 78px;
    line-height: 0.9;
    color: var(--brand-blue);
    letter-spacing: -1px;
  }
  .front-tagline {
    font-weight: 400;
    font-size: 27px;
    color: var(--ink-grey);
    margin-top: 2px;
  }
  .contact-block {
    position: absolute; left: 322px; top: 52px;
    color: var(--text-light);
  }
  .contact-name { font-weight: 700; font-size: 15px; }
  .contact-title { font-size: 13px; color: var(--text-muted); margin-top: 6px; }
  .contact-list { list-style: none; margin-top: 38px; }
  .contact-list li {
    display: flex; align-items: center; gap: 10px;
    font-size: 12.5px; color: var(--text-light);
    height: 22px;
  }
  .contact-icon { width: 12px; height: 12px; flex: none; }
  .social-square {
    width: 12px; height: 12px; flex: none;
    background: var(--brand-blue);
  }
</style>
</head>
<body>

  <section class="card card-back" aria-label="Card back">
    <div class="back-wordmark">Lox4ane</div>
    <div class="back-tagline">Executive Management</div>
  </section>

  <section class="card card-front" aria-label="Card front">
    <svg class="front-divider" width="560" height="320" viewBox="0 0 560 320">
      <defs>
        <linearGradient id="panelShade" x1="0" y1="0" x2="1" y2="1">
          <stop offset="0" stop-color="#3c3e41"/>
          <stop offset="1" stop-color="#26282a"/>
        </linearGradient>
      </defs>
      <path d="M330 0 H560 V320 H262 C300 230 318 120 300 0 Z" fill="url(#panelShade)"/>
      <path d="M300 0 C318 120 300 230 262 320 L242 320 C282 230 298 120 282 0 Z" fill="var(--brand-blue)"/>
      <path d="M300 0 C318 120 300 230 262 320 L256 320 C294 230 310 120 294 0 Z" fill="var(--card-white)"/>
      <path d="M262 40 C278 140 268 220 238 290 L234 288 C262 220 270 140 256 42 Z" fill="var(--brand-orange)"/>
    </svg>

    <div class="front-logo">
      <div class="front-wordmark">lox4</div>
      <div class="front-tagline">Management</div>
    </div>

    <div class="contact-block">
      <div class="contact-name">Dana Holt</div>
      <div class="contact-title">Principal</div>
      <ul class="contact-list">
        <li>
          <svg class="contact-icon" viewBox="0 0 12 12"><path d="M2 1h2.5l1 3-1.5 1a7 7 0 0 0 3 3l1-1.5 3 1V10a1 1 0 0 1-1 1C5 11 1 7 1 2a1 1 0 0 1 1-1z" fill="var(--brand-orange)"/></svg>
          555.014.2280
        </li>
        <li>
          <svg class="contact-icon" viewBox="0 0 12 12"><rect x="0.5" y="2.5" width="11" height="7" fill="none" stroke="var(--brand-orange)"/><path d="M0.5 2.5 6 7l5.5-4.5" fill="none" stroke="var(--brand-orange)"/></svg>
          lox4management@mailbox.com
        </li>
        <li><span class="social-square"></span>@lox4management</li>
        <li><span class="social-square"></span>DanaHoltExecMgmt</li>
      </ul>
    </div>
  </section>

</body>
</html>
```